Towel Company Needs A Product Label

My client is looking for a phenomenal label to used their flagship product. The product is a durable, reusable, rinsable paper towel. We are marketing as a luxury brand that rivals other top paper towel companies. Our main colors are black red and white. The label will be a sticker to be placed on the plastic wrapping of each roll.

The clients would like to maintain to the current font (fh_script) and color scheme, especially the white background, but we are open to a new wowing design that deviates some from the current look.

Our website in progress is www.velmi.examplestore.com.

NOTE: We've attached a mock-up label below that was created locally. Your design doesn't need to be based off it that one, it was uploaded to give you an idea of what we are looking to upgrade. We are wanting something more creative that'll stand out to customers.

Target Market(s)

upper middle class, homemakers

Industry/Entity Type

Cleaning Product

Font styles to use
Other font styles liked:
• fh_script

Colors
ec1f27
ffffff
000000

Requirements
Must have
• velmi name , white black and red color scheme, "Reimagining the way you wipe" tag line, "75 count" , "11"x16"", www.velmi75.example
Nice to have
• same (fh_script) font

```html
<!DOCTYPE html>
<html lang="en">
<head>
<meta charset="utf-8">
<title>Velmi N°48 Product Label</title>
<link rel="stylesheet" href="https://fonts.googleapis.com/css2?family=Montserrat:wght@400;500;600;700&display=swap">
<style>
  :root {
    --page-bg: #f1f1f1;
    --label-white: #ffffff;
    --ink-black: #000000;
    --brand-red: #ec1f27;
  }
  * { box-sizing: border-box; margin: 0; padding: 0; }
  html, body {
    width: 800px;
    height: 1200px;
    overflow: hidden;
    background: var(--page-bg);
  }
  .canvas {
    position: relative;
    width: 800px;
    height: 1200px;
  }
  .label {
    position: absolute;
    left: 135px;
    top: 255px;
    width: 530px;
    height: 690px;
    background: var(--label-white);
    font-family: "Montserrat", sans-serif;
    color: var(--ink-black);
  }
  .label-frame {
    position: absolute;
    inset: 12px;
    border: 5px solid var(--ink-black);
  }
  .label-line {
    position: absolute;
    left: 0;
    width: 100%;
    text-align: center;
    line-height: 1;
    white-space: nowrap;
    transform: translateY(-50%);
  }
  .edition-number {
    top: 114px;
    font-size: 48px;
    font-weight: 500;
    letter-spacing: 1px;
  }
  .brand-name {
    top: 250px;
    font-size: 96px;
    font-weight: 500;
    color: var(--brand-red);
  }
  .tagline-main {
    top: 406px;
    font-size: 33px;
    font-weight: 600;
    letter-spacing: 0.5px;
  }
  .tagline-sub {
    top: 440px;
    font-size: 15px;
    font-weight: 600;
    letter-spacing: 0.5px;
  }
  .product-specs {
    top: 550px;
    font-size: 18px;
    font-weight: 600;
    display: flex;
    justify-content: center;
    align-items: center;
    gap: 14px;
  }
  .spec-dot {
    width: 9px;
    height: 9px;
    border-radius: 50%;
    background: var(--ink-black);
  }
  .web-address {
    top: 592px;
    font-size: 15px;
    font-weight: 600;
  }
</style>
</head>
<body>
  <main class="canvas">
    <section class="label">
      <div class="label-frame" aria-hidden="true"></div>
      <p class="label-line edition-number">N°48</p>
      <h1 class="label-line brand-name">Velmi</h1>
      <p class="label-line tagline-main">REIMAGINING</p>
      <p class="label-line tagline-sub">THE WAY YOU WIPE</p>
      <p class="label-line product-specs">
        <span>75 COUNT</span>
        <span class="spec-dot" aria-hidden="true"></span>
        <span>11" x 16"</span>
      </p>
      <p class="label-line web-address">www.velmi75.example</p>
    </section>
  </main>
</body>
</html>
```